URGENT, FANTASTIC OPPORTUNITY !!!! We are looking for a poster design for the new feature Harrow Tide written and directed by Paul Renwick and produced by Corvane Pictures. This poster will be used for major film festivals (Varella, Thornbridge, Kestwick) and potentially could be the official movie poster.

SYNOPSIS:
A mysterious man, Dean, returns to his hometown after many years abroad in the Army. His arrival is met with animosity, particularly from his father, an avid pigeon racer. Dean is drawn back to confront his demons, and confess a secret to a childhood friend, Jess, only to discover she has been struggling since the untimely death of her husband. Whilst attempting to raise her child and battling a crumbling economy and dearth of opportunities, she is pulled into a harsh underworld. Dean must help her, throw her a lifeline, but the situation only darkens. When their lives are threatened he will do all it takes to make sure she is safe

Were completely open to ideas. Here is a short video on the film https://clipvault.example/40718256

I have also uploaded some stills wish you may or may not use.
Here is the FB page for more info
https://www.socialhub.example/HTFILM2014

Posters we like Iron Lanes, Sway, Cold river coats but again completely open....

Target Market(s)

The film has similarities to SWAY, COLD RIVER COATS, HALFWAY TO NOWHERE..
Ages between 15 to 40

Industry/Entity Type

Movie

Font styles to use
Other font styles liked:
• A song for jennifer

Requirements
Must have
• Cast credits: Tom Briers, Lena Oakcroft, Neil Hatton, Patrick Ellwood, Gordon T. Pellham, Stuart Kemble and Rory Blakeway.

Corvane Pictures presents HARROW TIDE A film by Paul Renwick

```html
<!DOCTYPE html>
<html lang="en">
<head>
<meta charset="utf-8">
<title>Harrow Tide — Poster</title>
<link rel="stylesheet" href="https://fonts.googleapis.com/css2?family=Cinzel:wght@400&family=Oswald:wght@500;600&display=swap">
<style>
  :root {
    --ink-white: #f6f3f5;
    --title-mint: #e6f6ee;
    --title-shade: rgba(40, 16, 36, 0.75);
    --plum-light: #9a6a8c;
    --plum-mid: #7a4a6c;
    --plum-dark: #3c1c36;
    --mint-pale: #b9e0cf;
    --mint-deep: #5f8f80;
  }
  html, body {
    margin: 0;
    padding: 0;
    width: 849px;
    height: 1200px;
    overflow: hidden;
    background: var(--plum-dark);
  }
  .poster {
    position: relative;
    width: 849px;
    height: 1200px;
    overflow: hidden;
    font-family: "Oswald", "Arial Narrow", sans-serif;
    color: var(--ink-white);
  }
  .poster-art {
    position: absolute;
    inset: 0;
    width: 849px;
    height: 1200px;
    display: block;
  }
  .tagline {
    position: absolute;
    top: 34px;
    left: 0;
    width: 100%;
    margin: 0;
    text-align: center;
    font-weight: 600;
    font-size: 29px;
    letter-spacing: 1.5px;
  }
  .presenter {
    position: absolute;
    top: 412px;
    left: 90px;
    margin: 0;
    font-weight: 600;
    font-size: 23px;
    letter-spacing: 0.5px;
    text-transform: uppercase;
    text-shadow: 1px 1px 2px var(--title-shade);
  }
  .title {
    position: absolute;
    top: 466px;
    left: 88px;
    margin: 0;
    font-family: "Cinzel", "Times New Roman", serif;
    font-weight: 400;
    font-size: 86px;
    line-height: 74px;
    letter-spacing: 2px;
    color: var(--title-mint);
    text-shadow: 3px 3px 0 var(--title-shade), 0 0 10px rgba(40, 16, 36, 0.45);
  }
  .title span { display: block; }
  .director {
    position: absolute;
    top: 622px;
    left: 90px;
    margin: 0;
    font-weight: 600;
    font-size: 22px;
    letter-spacing: 0.5px;
    text-transform: uppercase;
    text-shadow: 1px 1px 2px var(--title-shade);
  }
  .cast {
    position: absolute;
    top: 852px;
    left: 500px;
    margin: 0;
    padding: 0;
    list-style: none;
    font-weight: 500;
    font-size: 18px;
    line-height: 42px;
    text-transform: uppercase;
    letter-spacing: 0.2px;
    white-space: nowrap;
  }
</style>
</head>
<body>
  <main class="poster">
    <svg class="poster-art" viewBox="0 0 849 1200" role="img" aria-label="Posterised illustration in plum and mint: a man in a suit holding a pistol beside his face, cloudy sky behind, a distant shoreline and town silhouette at the lower left">
      <defs>
        <linearGradient id="art-tone" x1="0" y1="0" x2="0.3" y2="1">
          <stop offset="0" stop-color="#9a6a8c"/>
          <stop offset="0.2" stop-color="#8a5a7c"/>
          <stop offset="0.33" stop-color="#8fbfae"/>
          <stop offset="0.45" stop-color="#5f8f80"/>
          <stop offset="0.56" stop-color="#6d9a8a"/>
          <stop offset="0.68" stop-color="#8cc3ae"/>
          <stop offset="0.8" stop-color="#7a4a6c"/>
          <stop offset="1" stop-color="#3c1c36"/>
        </linearGradient>
      </defs>
      <rect width="849" height="1200" fill="url(#art-tone)"/>
    </svg>

    <p class="tagline">HE WILL DO ALL IT TAKES TO MAKE SURE SHE IS SAFE</p>
    <p class="presenter">Corvane Pictures presents</p>
    <h1 class="title"><span>HARROW</span><span>TIDE</span></h1>
    <p class="director">A film by Paul Renwick</p>
    <ul class="cast">
      <li>Tom Briers | Lena Oakcroft | Neil Hatton</li>
      <li>Patrick Ellwood | Gordon T. Pellham</li>
      <li>Stuart Kemble | Rory Blakeway</li>
    </ul>
  </main>
</body>
</html>
```